Business Consultancy Business Card Design

Business Card design required for Business Analysis and Project Consultancy business based in Scotland.

Company Name - Brackwell Consulting

Back - Company Logo

Front Details

Euan Brackwell
07402 916 254
euan.brackwell@brackwellconsulting.example
http://www.brackwellconsulting.example

Colours should match the logo colours but I am open to design ideas.

```html
<!DOCTYPE html>
<html lang="en">
<head>
<meta charset="utf-8">
<title>Brackwell Consulting – Business Cards</title>
<link rel="stylesheet" href="https://fonts.googleapis.com/css2?family=Arimo:wght@400&display=swap">
<style>
  :root {
    --backdrop: #e9eaec;
    --brand-blue: #1e9ad6;
    --brand-green: #5db732;
    --band-white: #ffffff;
    --ink-grey: #555a5e;
    --rule-grey: #6b7074;
    --card-shadow: rgba(0, 0, 0, 0.18);
  }
  * { box-sizing: border-box; margin: 0; padding: 0; }
  html, body {
    width: 1200px;
    height: 873px;
    overflow: hidden;
    background: var(--backdrop);
    font-family: "Arimo", Arial, sans-serif;
  }
  .stage {
    position: relative;
    width: 1200px;
    height: 873px;
  }
  .card {
    position: absolute;
    top: 286px;
    width: 500px;
    height: 300px;
    overflow: hidden;
    box-shadow: 0 6px 18px var(--card-shadow);
    background: var(--band-white);
  }
  .card--front { left: 70px; }
  .card--back { left: 630px; }

  .band { position: absolute; left: 0; width: 100%; }
  .band--blue { background: var(--brand-blue); top: 0; }
  .band--green { background: var(--brand-green); bottom: 0; }

  /* Front */
  .card--front .band--blue { height: 70px; }
  .card--front .band--green { height: 60px; }
  .front-circle {
    position: absolute;
    left: 20px;
    top: 30px;
    width: 180px;
    height: 180px;
    border-radius: 50%;
    background: rgba(255, 255, 255, 0.82);
  }
  .holder-name {
    position: absolute;
    right: 310px;
    top: 86px;
    text-align: right;
    color: var(--ink-grey);
    font-size: 25px;
    line-height: 29px;
    letter-spacing: 0.5px;
    text-transform: uppercase;
  }
  .name-rule {
    position: absolute;
    left: 200px;
    top: 84px;
    width: 2px;
    height: 62px;
    background: var(--rule-grey);
  }
  .contact-list {
    position: absolute;
    left: 212px;
    top: 150px;
    list-style: none;
    color: var(--ink-grey);
    font-size: 11px;
    line-height: 20px;
  }
  .contact-list li { display: flex; align-items: center; gap: 8px; }
  .contact-icon { width: 12px; height: 12px; flex: none; }

  /* Back */
  .card--back .band--blue { height: 112px; }
  .card--back .band--green { height: 124px; }
  .brand-circle {
    position: absolute;
    left: 56px;
    top: 106px;
    width: 76px;
    height: 76px;
    margin-top: -20px;
    border-radius: 50%;
    background: var(--band-white);
  }
  .brand-rule {
    position: absolute;
    left: 146px;
    top: 118px;
    width: 2px;
    height: 52px;
    background: var(--rule-grey);
  }
  .brand-name {
    position: absolute;
    left: 160px;
    top: 130px;
    color: var(--ink-grey);
    font-size: 24px;
    line-height: 28px;
    letter-spacing: 0.5px;
    text-transform: uppercase;
    white-space: nowrap;
  }
</style>
</head>
<body>
<main class="stage">
  <section class="card card--front" aria-label="Business card front">
    <div class="band band--blue"></div>
    <div class="band band--green"></div>
    <div class="front-circle"></div>
    <h1 class="holder-name">Euan<br>Brackwell</h1>
    <div class="name-rule"></div>
    <ul class="contact-list">
      <li>
        <svg class="contact-icon" viewBox="0 0 12 12" aria-hidden="true">
          <rect x="3" y="0.5" width="6" height="11" rx="1.2" fill="none" stroke="#555a5e" stroke-width="1"/>
          <rect x="4" y="2" width="4" height="6" fill="#555a5e"/>
          <circle cx="6" cy="9.8" r="0.7" fill="#555a5e"/>
        </svg>
        <span>07402 916 254</span>
      </li>
      <li>
        <svg class="contact-icon" viewBox="0 0 12 12" aria-hidden="true">
          <rect x="0.5" y="2" width="11" height="8" fill="#555a5e"/>
          <path d="M0.5 2 L6 6.5 L11.5 2 M0.5 10 L4.5 5.5 M11.5 10 L7.5 5.5" fill="none" stroke="#fff" stroke-width="0.9"/>
        </svg>
        <span>euan.brackwell@brackwellconsulting.example</span>
      </li>
      <li>
        <svg class="contact-icon" viewBox="0 0 12 12" aria-hidden="true">
          <circle cx="6" cy="6" r="5.3" fill="none" stroke="#555a5e" stroke-width="0.9"/>
          <ellipse cx="6" cy="6" rx="2.3" ry="5.3" fill="none" stroke="#555a5e" stroke-width="0.8"/>
          <path d="M0.7 6 H11.3 M1.5 3.4 H10.5 M1.5 8.6 H10.5" stroke="#555a5e" stroke-width="0.8"/>
        </svg>
        <span>http://www.brackwellconsulting.example</span>
      </li>
    </ul>
  </section>

  <section class="card card--back" aria-label="Business card back">
    <div class="band band--blue"></div>
    <div class="band band--green"></div>
    <div class="brand-circle"></div>
    <div class="brand-rule"></div>
    <h2 class="brand-name">Brackwell Consulting</h2>
  </section>
</main>
</body>
</html>
```